Automotive Locksmiith company needs a website design and mobile website

We need a website design and a mobile design for an automotive locksmith company called Halvern Keyworks LLC.We are based in the center of the Dallas-Fort Worth Metroplex. We have a website that was directed more towards the towing services we also offer. We would like to have it more towards our locksmith products. Our main services include:
Auto keys duplication
Cutting of new car keys
Car Lockouts
Laser key replacement
Cutting keys by code
Broken key extractions
Production of transponder keys
Key fob programming
Door lock repairs
Ignition repairs/replacement
We work on 95% of the automotive market that includes Vorla, Tessin, QRT, Pembrook, Marquenne, Dunmoral, Brask, VX, Sorvalo, Kelto, Zephrane, Oru, Hadley, Norax, Tabori, Valdrenne, Quillon, Pipo, Runel Okarawe , Brevik, Solumé, Drennhofer, Kestra.
We are one of the most affordable services in the DFW area . Our prices for transponder copies start at $35 per key. We provide services for high-end vehicles also as QRT and Valdrenne. We can program the new proximity keys for Tabori Vehicles 2013-up. We also work on the new Pell Vehicles 20-13 and up including the Pell Arden head remote key.
We would like to have a similar style to the website we already have with the option to schedule an appointment on the mobile website. This mobile application will deliver an email when a new customer is requiring the service. It will ask for Year, Make, Model , Service to be performed( Key copy, Lockout, Lost Key, Change Ignition lock, change door lock, Other services.) Description of the service to be performed, Address, Select time of service.
Our current website is halvernkeyworks.example

Reason: Need pictures of webpages inside design (about us , location etc) and mobile pictures( how website looks in Quorra / android)

Automotive

• check word attachment

```html
<!DOCTYPE html>
<html lang="en">
<head>
<meta charset="utf-8">
<title>Halvern Keyworks LLC – Mobile</title>
<link href="https://fonts.googleapis.com/css2?family=Roboto:wght@400;700&family=Roboto+Condensed:wght@400;700&family=Kalam:wght@400&display=swap" rel="stylesheet">
<style>
  :root {
    --page-bg: #1a1a1a;
    --topbar-bg: #2e2e2e;
    --header-bg: #262626;
    --panel-bg: #1d1d1d;
    --panel-border: #3a3a3a;
    --field-bg: #3a3c44;
    --field-text: #8b8e98;
    --label-text: #d9d9d9;
    --accent: #4fa3c9;
    --accent-dark: #3a88ad;
    --muted: #9a9a9a;
    --white: #ffffff;
    --band-light: #f2f2f2;
    --photo-tone: #6f7c8c;
  }
  * { box-sizing: border-box; margin: 0; padding: 0; }
  html, body {
    width: 1038px; height: 1200px; overflow: hidden;
    background: var(--page-bg);
    font-family: "Roboto", Arial, sans-serif;
  }
  .mobile-page { width: 1038px; height: 1200px; display: flex; flex-direction: column; }

  .top-bar {
    height: 58px; background: var(--topbar-bg);
    display: flex; align-items: center; gap: 44px; padding: 0 40px;
    color: var(--muted); font-size: 18px;
  }
  .top-bar .contact-item { display: flex; align-items: center; gap: 10px; }

  .site-header {
    height: 112px; background: var(--header-bg);
    display: flex; align-items: center; justify-content: space-between; padding: 0 40px;
    border-bottom: 1px solid #111;
  }
  .brand { display: flex; align-items: center; gap: 16px; }
  .brand-mark { width: 46px; height: 46px; background: var(--accent); }
  .brand-name { font-family: "Roboto Condensed", sans-serif; font-weight: 700; font-size: 30px; color: var(--white); }
  .menu-select {
    width: 360px; height: 44px; background: var(--white); border: 1px solid #bbb;
    display: flex; align-items: center; justify-content: space-between; padding: 0 14px;
    font-size: 17px; color: #333; font-weight: 700;
  }

  .booking-panel {
    margin: 22px 40px 0; padding: 26px 34px 30px;
    background: var(--panel-bg); border: 2px solid var(--panel-border);
  }
  .field-label { font-family: "Roboto Condensed", sans-serif; font-weight: 700; font-size: 25px; color: var(--label-text); margin: 18px 0 8px; }
  .select-field {
    height: 54px; background: var(--field-bg);
    display: flex; align-items: center; justify-content: space-between; padding: 0 18px;
    font-size: 21px; color: var(--field-text);
  }
  .search-button {
    margin-top: 28px; height: 72px; background: var(--accent);
    border-bottom: 4px solid var(--accent-dark);
    display: flex; align-items: center; justify-content: center;
    color: var(--white); font-family: "Roboto Condensed", sans-serif; font-weight: 700; font-size: 30px;
  }

  .offer-panel {
    margin: 22px 40px 0; padding: 24px 34px;
    background: var(--panel-bg); border: 2px solid var(--panel-border);
  }
  .offer-kicker { font-size: 19px; color: var(--muted); }
  .offer-title { font-family: "Roboto Condensed", sans-serif; font-weight: 700; font-size: 38px; color: var(--white); margin: 4px 0 12px; }
  .offer-text { font-size: 16px; line-height: 1.45; color: var(--muted); margin-bottom: 10px; }

  .accent-strip { height: 12px; background: var(--accent); margin-top: 24px; }
  .about-band { flex: 1; background: var(--band-light); padding: 18px 40px 0; }
  .about-title { font-family: "Kalam", cursive; font-size: 44px; color: #222; line-height: 1.1; }
  .about-photo { margin-top: 10px; height: 120px; background: linear-gradient(90deg, var(--photo-tone), #46505c); }
</style>
</head>
<body>
<main class="mobile-page">
  <div class="top-bar">
    <span class="contact-item">
      <svg width="18" height="18" viewBox="0 0 24 24" fill="#9a9a9a"><path d="M6.6 10.8a15 15 0 0 0 6.6 6.6l2.2-2.2c.3-.3.7-.4 1-.2 1.1.4 2.3.6 3.6.6.6 0 1 .4 1 1V20c0 .6-.4 1-1 1A17 17 0 0 1 3 4c0-.6.4-1 1-1h3.5c.6 0 1 .4 1 1 0 1.3.2 2.5.6 3.6.1.3 0 .7-.2 1z"/></svg>
      214.555.0147
    </span>
    <span class="contact-item">
      <svg width="16" height="20" viewBox="0 0 24 30" fill="#9a9a9a"><path d="M12 0C5.4 0 0 5.2 0 11.7 0 20.5 12 30 12 30s12-9.5 12-18.3C24 5.2 18.6 0 12 0zm0 16a4.5 4.5 0 1 1 0-9 4.5 4.5 0 0 1 0 9z"/></svg>
      Serving the Dallas-Fort Worth Metroplex
    </span>
  </div>

  <header class="site-header">
    <div class="brand">
      <span class="brand-mark"></span>
      <span class="brand-name">Halvern Keyworks LLC</span>
    </div>
    <div class="menu-select">
      MENU
      <svg width="14" height="10" viewBox="0 0 14 10"><path d="M0 0h14L7 10z" fill="#333"/></svg>
    </div>
  </header>

  <section class="booking-panel">
    <div class="select-field"><span></span><svg width="14" height="10" viewBox="0 0 14 10"><path d="M0 0h14L7 10z" fill="#c8c8c8"/></svg></div>
    <div class="field-label">Year :</div>
    <div class="select-field">Any<svg width="14" height="10" viewBox="0 0 14 10"><path d="M0 0h14L7 10z" fill="#c8c8c8"/></svg></div>
    <div class="field-label">Make :</div>
    <div class="select-field">Any<svg width="14" height="10" viewBox="0 0 14 10"><path d="M0 0h14L7 10z" fill="#c8c8c8"/></svg></div>
    <div class="field-label">Model :</div>
    <div class="select-field">Any<svg width="14" height="10" viewBox="0 0 14 10"><path d="M0 0h14L7 10z" fill="#c8c8c8"/></svg></div>
    <div class="field-label">Service to be performed :</div>
    <div class="select-field">Any<svg width="14" height="10" viewBox="0 0 14 10"><path d="M0 0h14L7 10z" fill="#c8c8c8"/></svg></div>
    <div class="search-button">Search</div>
  </section>

  <section class="offer-panel">
    <p class="offer-kicker">Professional Automotive Locksmith Services</p>
    <h1 class="offer-title">Special Price For Used Car Dealerships!</h1>
    <p class="offer-text">We are proud to offer used car dealerships a special rate on transponder key copies, lost key replacement and key fob programming. Ask about volume pricing for your lot and let our mobile technicians come to you across the whole Metroplex.</p>
    <p class="offer-text">Our licensed team works on most makes and models, cuts keys by code and repairs ignition and door locks on site. Call today to schedule an appointment that fits your time.</p>
  </section>

  <div class="accent-strip"></div>
  <section class="about-band">
    <h2 class="about-title">About Us</h2>
    <div class="about-photo" role="img" aria-label="Photo of the locksmith team and service van"></div>
  </section>
</main>
</body>
</html>
```